Landing Page für Kornwiese-Prüfset.de
Zielgruppe
Domain: Kornwiese-Prüfset.de
THC Schnelltests mit gringer Anzeigegrenze mit 5ng/ml, ausgerichtet auf die Selbstkontrolle für die Fahrtauglichkeit (Grenze im Gesetz 3,5ng/ml)
Farbe: grün
Anregung siehe Bild
Aufgabenstellung
- Conversionoptimiert
- Soll auf unseren Webshop www.rv-vitalis.de verlinken

```html
<!DOCTYPE html>
<html lang="de">
<head>
<meta charset="utf-8">
<title>Kornwiese-Prüfset.de – THC Schnelltests</title>
<link rel="stylesheet" href="https://fonts.googleapis.com/css2?family=Montserrat:ital,wght@0,700;0,800;1,500;1,600;1,700;1,800;1,900&display=swap">
<style>
  :root {
    --stage: #a7c097;
    --green-mid: #48824a;
    --green-light: #8aba5e;
    --green-dark: #0b3d0b;
    --green-left: #3f7c3f;
    --headline-green: #86bb5e;
    --cream: #f8f0d8;
    --white: #ffffff;
    --button-shadow: #2f6a2f;
  }
  * { margin: 0; padding: 0; box-sizing: border-box; }
  html, body { width: 1200px; height: 1117px; overflow: hidden; }
  body {
    background: var(--stage);
    font-family: "Montserrat", sans-serif;
    position: relative;
  }
  .banner {
    position: absolute;
    left: 64px; top: 374px;
    width: 1072px; height: 368px;
    overflow: hidden;
    box-shadow: 6px 8px 10px rgba(0,0,0,0.15);
  }
  .banner__background { position: absolute; inset: 0; }
  .headline {
    position: absolute;
    left: 48px; top: 26px;
    font-weight: 900; font-style: italic;
    font-size: 79px; line-height: 72px;
    letter-spacing: -1px;
    text-shadow: 3px 4px 6px rgba(0,0,0,0.3);
  }
  .headline__top { color: var(--headline-green); display: block; }
  .headline__bottom { color: var(--cream); display: block; }
  .tagline {
    position: absolute; left: 53px; top: 181px;
    color: var(--cream);
    font-weight: 700; font-style: italic; font-size: 14.5px;
    white-space: nowrap;
  }
  .offer {
    position: absolute; left: 36px; top: 219px; width: 320px;
    text-align: center; color: var(--cream);
  }
  .offer__title {
    font-weight: 900; font-style: italic; font-size: 27.5px;
    line-height: 32px;
    white-space: nowrap;
    text-shadow: 2px 3px 4px rgba(0,0,0,0.3);
  }
  .offer__text {
    font-weight: 600; font-style: italic; font-size: 14.5px;
    line-height: 17.5px; text-transform: uppercase;
    white-space: nowrap;
  }
  .limit-badge {
    position: absolute; left: 373px; top: 176px;
    width: 170px; height: 170px; border-radius: 50%;
    background: linear-gradient(180deg, #fbeeb8 0%, #a9c872 25%, var(--green-light) 45%);
    box-shadow: 4px 6px 12px rgba(0,0,0,0.3);
    display: flex; align-items: center; justify-content: center;
    text-align: center; color: var(--white);
    font-weight: 900; font-style: italic; font-size: 25px; line-height: 27px;
    text-shadow: 1px 2px 3px rgba(0,0,0,0.25);
  }
  .product-photo {
    position: absolute; left: 563px; top: 87px;
    width: 297px; height: 265px;
    background: radial-gradient(ellipse at center, rgba(240,244,246,0.85) 0%, rgba(220,230,235,0.5) 45%, rgba(72,130,74,0) 72%);
  }
  .plant-photo {
    position: absolute; left: 784px; top: 0;
    width: 288px; height: 238px;
    background: radial-gradient(ellipse at 70% 45%, #8fb04e 0%, #5f9a3a 40%, rgba(72,130,74,0) 75%);
  }
  .cta {
    position: absolute; left: 805px; top: 293px;
    width: 228px; height: 36px; border-radius: 4px;
    background: var(--green-light);
    box-shadow: 0 4px 0 var(--button-shadow);
    color: var(--white); font-weight: 800; font-size: 22px;
    display: flex; align-items: center; justify-content: center;
    text-decoration: none; letter-spacing: 0.5px;
  }
</style>
</head>
<body>
  <section class="banner">
    <svg class="banner__background" viewBox="0 0 1072 368" width="1072" height="368" aria-hidden="true">
      <defs>
        <linearGradient id="darkPanel" x1="0" y1="0" x2="1" y2="0">
          <stop offset="0" stop-color="#3f7c3f"/>
          <stop offset="0.55" stop-color="#11481a"/>
          <stop offset="1" stop-color="#063a08"/>
        </linearGradient>
        <radialGradient id="bubble" cx="0.35" cy="0.35" r="0.7">
          <stop offset="0" stop-color="#7fb35f"/>
          <stop offset="1" stop-color="#3c7a3a"/>
        </radialGradient>
      </defs>
      <rect width="1072" height="368" fill="var(--green-mid)"/>
      <path d="M0 0 L830 0 C720 170 410 200 355 368 L0 368 Z" fill="var(--green-light)"/>
      <path d="M0 0 L751 0 C640 150 380 170 343 368 L0 368 Z" fill="url(#darkPanel)"/>
      <g fill="url(#bubble)">
        <circle cx="634" cy="34" r="9"/>
        <circle cx="615" cy="82" r="5"/>
        <circle cx="545" cy="82" r="3.5"/>
        <circle cx="606" cy="129" r="3"/>
        <circle cx="573" cy="31" r="1.8"/>
        <circle cx="683" cy="44" r="2.5"/>
        <circle cx="354" cy="259" r="4"/>
        <circle cx="345" cy="310" r="2.5"/>
        <circle cx="312" cy="331" r="6"/>
      </g>
    </svg>

    <h1 class="headline">
      <span class="headline__top">MACH DEN</span>
      <span class="headline__bottom">SELBSTTEST.</span>
    </h1>
    <p class="tagline">GEFÄHRDE NICHT DEINEN FÜHRERSCHEIN!</p>

    <div class="offer">
      <h2 class="offer__title">THC SCHNELLTESTS</h2>
      <p class="offer__text">Mit gringer Anzeigegrenze<br>mit 5ng/ml, ausgerichtet auf die<br>Selbstkontrolle für die<br>Fahrtauglichkeit</p>
    </div>

    <div class="limit-badge">Grenze<br>im Gesetz<br>3,5ng/ml</div>

    <div class="product-photo" role="img" aria-label="Produktfoto: THC-Testkit mit Beutel, Testkassette, Pipette und Trockenmittel"></div>
    <div class="plant-photo" role="img" aria-label="Foto: Cannabisblätter und Blüte"></div>

    <a class="cta" href="#shop">JETZT PRÜFEN</a>
  </section>
</body>
</html>
```